Business Card Design Project

New business cards that encompass our new logo.
Looking for -
Name, Title, Cell Phone, Email, Address (2 lines), Main Phone, Fax, and website.
Reason: I don't like the graphics used to show phone, fax, cell, email, web, and address.....
I like the double sided cards with logo's on the back. I do not like the logos for phone, fax, cell, address, email, or web.

```html
<!DOCTYPE html>
<html lang="en">
<head>
<meta charset="utf-8">
<title>Northbay Kitchen Supply – Business Card</title>
<link rel="stylesheet" href="https://fonts.googleapis.com/css2?family=Montserrat:wght@500;600;700&family=Arimo:wght@400;500;700&display=swap">
<style>
  :root {
    --navy: #1d4584;
    --red: #c9313f;
    --white: #ffffff;
    --grey-text: #6d6e71;
    --backdrop: #e9eaec;
  }
  * { margin: 0; padding: 0; box-sizing: border-box; }
  html, body {
    width: 1200px;
    height: 600px;
    overflow: hidden;
    background: var(--backdrop);
  }
  .canvas {
    position: relative;
    width: 1200px;
    height: 600px;
  }
  .card {
    position: absolute;
    top: 152px;
    width: 467px;
    height: 278px;
    box-shadow: 0 4px 14px rgba(0, 0, 0, 0.12);
    overflow: hidden;
  }

  /* Back side */
  .card-back {
    left: 93px;
    background: var(--navy);
    color: var(--white);
  }
  .card-back .wordmark {
    position: absolute;
    left: 0;
    right: 0;
    top: 122px;
    text-align: center;
    font-family: "Montserrat", sans-serif;
    font-weight: 700;
    color: var(--white);
    line-height: 1;
  }
  .wordmark .wordmark-main {
    display: block;
    font-size: 44px;
    letter-spacing: 0.5px;
  }
  .wordmark .wordmark-sub {
    display: block;
    font-size: 17px;
    letter-spacing: 2.4px;
    margin-top: 8px;
  }
  .card-back .website {
    position: absolute;
    left: 0;
    right: 0;
    top: 245px;
    text-align: center;
    font-family: "Montserrat", sans-serif;
    font-weight: 600;
    font-size: 11.5px;
    letter-spacing: 2.2px;
    text-transform: uppercase;
  }

  /* Front side */
  .card-front {
    left: 638px;
    background: var(--white);
  }
  .card-front .wordmark {
    position: absolute;
    left: 14px;
    width: 250px;
    top: 136px;
    text-align: center;
    font-family: "Montserrat", sans-serif;
    font-weight: 700;
    color: var(--navy);
    line-height: 1;
  }
  .card-front .wordmark .wordmark-main { font-size: 40px; }
  .card-front .wordmark .wordmark-sub { font-size: 15px; letter-spacing: 2.2px; }

  .divider {
    position: absolute;
    left: 275px;
    top: 54px;
    width: 2px;
    height: 164px;
    background: var(--navy);
  }
  .contact {
    position: absolute;
    left: 284px;
    top: 60px;
    width: 175px;
    font-family: "Arimo", sans-serif;
    font-weight: 500;
    font-size: 13px;
    color: var(--grey-text);
    line-height: 17px;
    white-space: nowrap;
  }
  .contact .person-name {
    font-family: "Montserrat", sans-serif;
    font-weight: 600;
    font-size: 14.5px;
    color: var(--red);
    letter-spacing: 0.3px;
  }
  .contact .address { margin-top: 20px; }
  .contact .details {
    margin-top: 18px;
    display: grid;
    grid-template-columns: 52px auto;
    row-gap: 2px;
  }
  .details dt { font-weight: 700; color: var(--navy); }
  .details dd { color: var(--grey-text); }

  .stripe-red {
    position: absolute;
    left: 0; right: 0;
    top: 256px;
    height: 3px;
    background: var(--red);
  }
  .stripe-navy {
    position: absolute;
    left: 0; right: 0;
    top: 262px;
    height: 16px;
    background: var(--navy);
  }
</style>
</head>
<body>
<main class="canvas">
  <section class="card card-back" aria-label="Card back">
    <div class="wordmark">
      <span class="wordmark-main">NORTHBAY</span>
      <span class="wordmark-sub">KITCHEN SUPPLY</span>
    </div>
    <p class="website">www.northbaysupply.com</p>
  </section>

  <section class="card card-front" aria-label="Card front">
    <div class="wordmark">
      <span class="wordmark-main">NORTHBAY</span>
      <span class="wordmark-sub">KITCHEN SUPPLY</span>
    </div>
    <div class="divider"></div>
    <div class="contact">
      <p class="person-name">DALE MORGAN</p>
      <p class="person-title">Manager / CEO</p>
      <p class="address">1870 Cedar Ave. #310<br>Fairview, TX 75069</p>
      <dl class="details">
        <dt>Phone:</dt><dd>+1 555 014 2276</dd>
        <dt>Email:</dt><dd>dm@northbayks.com</dd>
        <dt>Web:</dt><dd>northbayks.com</dd>
      </dl>
    </div>
    <div class="stripe-red"></div>
    <div class="stripe-navy"></div>
  </section>
</main>
</body>
</html>
```